CD Cover für junge Pop-Rock Band
Sehr kreative vorschläge. mehrere designs, die alle unter den top-favoriten für uns waren. änderungen und anpassungen stets schnell umgesetzt und auch nach gewinner-auswahl noch weiter zusammen gearbeitet bevor das endgültige design übergeben wurde.
Zielgruppe
Wir sind eine junge Band aus München und machen ausschließlich eigene Songs im Bereich Pop-Rock. Durch Einflüsse aus verschiedenen anderen Genres wie Funk, Reggae und Britpop grenzen sich unsere Songs von typischem Mainstream-Pop ab. Unsere Zielgruppe setzt sich aus Personen verschiedener Altersgruppen zusammen, der Fokus liegt jedoch auf Mitte Zwanzig- bis Mitte Dreißig-Jährigen.
Homepage: www.lemurgroove.com
Chatterly: www.facebook.com/lemurgrooveband
Aufgabenstellung
Wir benötigen ein Design für unsere neue EP "Paper Sails". Diese wird in Form eines DigiPacks veröffentlicht werden. Daher werden Designs für Vorderseite, Rückseite, zwei Innenseiten sowie die CD selbst benötigt.
Folgendes sollte auf den jeweiligen Seiten enthalten sein:
Vorderseite:
- Bandschriftzug (siehe Anhang)
- Name der EP: Paper Sails
Rückseite:
- Trackliste (1.Velvet Stair, 2.Show Us Why, 3.Harbor Glow, 4.Can We Stay, 5.Quiet Hours)
- Credits (Recording by ..., Mix by ..., Mastering by ..., etc. -> wird noch festgesetzt)
Anmerkung:
Die roten Kratzer aus dem Bandlogo können bei Bedarf frei verwendet werden hinsichtlich Farbe, Muster, Gestaltung, Größe, etc.
Wir möchten keine Bilder von uns (z.B. von unserer Homepage, Chatterly, etc) auf der CD.

```html
<!DOCTYPE html>
<html lang="de">
<head>
<meta charset="utf-8">
<title>Lemurgroove – Paper Sails DigiPack</title>
<link href="https://fonts.googleapis.com/css2?family=Josefin+Sans:wght@300&family=Montserrat:wght@600;700&family=Oswald:wght@400&display=swap" rel="stylesheet">
<style>
  :root {
    --canvas: #e4e4e0;
    --paper: #ffffff;
    --ink: #1d1b22;
    --muted: #a9a9ad;
    --track: #8a8a8e;
    --credit: #55525a;
    --magenta: #a02c8c;
    --violet: #5b2f95;
    --indigo: #2c2c6e;
    --peach: #f2cfb4;
    --blush: #f6c9d8;
    --rim: #c8c8c8;
  }
  html, body {
    margin: 0;
    width: 1066px;
    height: 1200px;
    overflow: hidden;
    background: var(--canvas);
  }
  .sheet {
    position: relative;
    width: 1066px;
    height: 1200px;
  }
  .panel {
    position: absolute;
    width: 340px;
    height: 302px;
    background: var(--paper);
    box-shadow: 0 2px 4px rgba(0,0,0,.25);
    overflow: hidden;
  }
  .panel--front { left: 30px;  top: 250px; }
  .panel--back  { left: 393px; top: 250px; }
  .panel--inside-left  { left: 211px; top: 620px; }
  .panel--inside-right { left: 574px; top: 620px; }

  .artwork { position: absolute; }
  .artwork--front {
    left: 10px; top: 0; width: 320px; height: 290px;
    background:
      radial-gradient(ellipse 60px 55px at 60px 60px, var(--peach), transparent 70%),
      radial-gradient(ellipse 70px 60px at 140px 90px, var(--indigo), transparent 72%),
      radial-gradient(ellipse 55px 50px at 200px 45px, var(--violet), transparent 70%),
      radial-gradient(ellipse 60px 55px at 90px 180px, var(--magenta), transparent 72%),
      radial-gradient(ellipse 55px 50px at 160px 240px, var(--magenta), transparent 72%),
      radial-gradient(ellipse 45px 40px at 255px 225px, var(--violet), transparent 72%),
      radial-gradient(ellipse 70px 40px at 45px 120px, var(--blush), transparent 72%);
  }
  .artwork--back {
    left: 110px; top: 0; width: 230px; height: 302px;
    background:
      radial-gradient(ellipse 60px 50px at 110px 30px, var(--peach), transparent 72%),
      radial-gradient(ellipse 70px 80px at 120px 150px, #8a5a3a, transparent 72%),
      radial-gradient(ellipse 60px 70px at 80px 230px, var(--violet), transparent 72%),
      radial-gradient(ellipse 55px 60px at 170px 200px, var(--magenta), transparent 72%),
      radial-gradient(ellipse 40px 40px at 200px 60px, var(--indigo), transparent 72%);
  }
  .artwork--inside-left {
    left: 0; top: 0; width: 340px; height: 302px;
    background:
      radial-gradient(ellipse 70px 50px at 50px 70px, var(--magenta), transparent 72%),
      radial-gradient(ellipse 80px 60px at 150px 60px, var(--blush), transparent 72%),
      radial-gradient(ellipse 60px 55px at 260px 40px, var(--peach), transparent 72%),
      radial-gradient(ellipse 70px 60px at 170px 150px, var(--indigo), transparent 72%),
      radial-gradient(ellipse 80px 60px at 170px 230px, var(--magenta), transparent 72%),
      radial-gradient(ellipse 70px 40px at 110px 270px, var(--peach), transparent 72%);
  }
  .artwork--inside-right {
    left: 0; top: 0; width: 340px; height: 302px;
    background:
      radial-gradient(ellipse 120px 60px at 180px 45px, var(--peach), transparent 72%),
      radial-gradient(ellipse 80px 55px at 150px 125px, var(--violet), transparent 72%),
      radial-gradient(ellipse 50px 45px at 250px 105px, var(--magenta), transparent 72%),
      radial-gradient(ellipse 60px 70px at 210px 210px, var(--blush), transparent 72%),
      radial-gradient(ellipse 60px 55px at 295px 270px, var(--magenta), transparent 72%);
  }

  .band-name {
    font-family: "Josefin Sans", sans-serif;
    font-weight: 300;
    color: var(--ink);
    text-transform: uppercase;
    letter-spacing: -0.3px;
    margin: 0;
    line-height: 1;
    white-space: nowrap;
  }
  .release-title {
    font-family: "Montserrat", sans-serif;
    font-weight: 600;
    color: var(--muted);
    letter-spacing: 1.5px;
    text-transform: uppercase;
    margin: 0;
    line-height: 1;
    white-space: nowrap;
  }
  .front-title {
    position: absolute;
    right: 12px; top: 150px;
    text-align: right;
  }
  .front-title .band-name { font-size: 20px; }
  .front-title .release-title { font-size: 10px; margin-top: 5px; }

  .tracklist {
    position: absolute;
    left: 24px; top: 26px;
    margin: 0; padding: 0;
    list-style: none;
    font-family: "Montserrat", sans-serif;
    font-weight: 700;
    color: var(--track);
    text-transform: uppercase;
  }
  .tracklist li {
    font-size: 16px;
    letter-spacing: 1.5px;
    line-height: 22px;
  }
  .tracklist .track-no {
    display: inline-block;
    width: 22px;
    font-size: 10px;
  }
  .credits {
    position: absolute;
    left: 0; right: 0;
    font-family: "Oswald", sans-serif;
    font-size: 7px;
    color: var(--credit);
    text-align: center;
    text-transform: uppercase;
    margin: 0;
  }
  .credits--first  { top: 256px; }
  .credits--second { top: 272px; }

  .lyrics {
    position: absolute;
    left: 30px; top: 220px;
    margin: 0;
    font-family: "Montserrat", sans-serif;
    font-weight: 700;
    font-size: 12.5px;
    line-height: 13px;
    letter-spacing: 0.5px;
    color: var(--ink);
    text-transform: uppercase;
    opacity: .85;
  }

  .disc {
    position: absolute;
    left: 756px; top: 256px;
    width: 290px; height: 290px;
  }
  .disc-band { font-family: "Josefin Sans", sans-serif; font-weight: 300; font-size: 18px; fill: var(--ink); }
  .disc-release { font-family: "Montserrat", sans-serif; font-weight: 600; font-size: 8px; letter-spacing: 1.5px; fill: var(--muted); }
  .disc-tracks { font-family: "Montserrat", sans-serif; font-weight: 600; font-size: 6.5px; letter-spacing: 0.5px; fill: var(--credit); }
</style>
</head>
<body>
<main class="sheet">

  <section class="panel panel--front" aria-label="Vorderseite">
    <div class="artwork artwork--front" role="img" aria-label="Tintenwolken in Magenta, Violett und Pfirsich mit polygonalen Facetten, darin ein Bandmitglied mit Mütze im Profil"></div>
    <div class="front-title">
      <p class="band-name">Lemurgroove</p>
      <p class="release-title">Paper Sails</p>
    </div>
  </section>

  <section class="panel panel--back" aria-label="Rückseite">
    <div class="artwork artwork--back" role="img" aria-label="Tintenwolken in Violett und Magenta, darin eine Person in brauner Jacke von hinten"></div>
    <ol class="tracklist">
      <li><span class="track-no">1.</span>Velvet Stair</li>
      <li><span class="track-no">2.</span>Show Us Why</li>
      <li><span class="track-no">3.</span>Harbor Glow</li>
      <li><span class="track-no">4.</span>Can We Stay</li>
      <li><span class="track-no">5.</span>Quiet Hours</li>
    </ol>
    <p class="credits credits--first">Recording by Klangmeier | Mix by Tonhuber | Mastering by Pegelstein</p>
    <p class="credits credits--second">Recording by Klangmeier | Mix by Tonhuber | Mastering by Pegelstein</p>
  </section>

  <svg class="disc" viewBox="0 0 290 290" aria-label="CD-Label">
    <defs>
      <radialGradient id="disc-ink" cx="0.45" cy="0.3" r="0.6">
        <stop offset="0" stop-color="#f2cfb4"/>
        <stop offset="0.45" stop-color="#5b2f95"/>
        <stop offset="0.8" stop-color="#a02c8c"/>
        <stop offset="1" stop-color="#ffffff"/>
      </radialGradient>
      <clipPath id="disc-clip"><circle cx="145" cy="145" r="143"/></clipPath>
      <path id="disc-rim" d="M 15 145 A 130 130 0 0 0 275 145 A 130 130 0 0 0 257.6 80"/>
    </defs>
    <circle cx="145" cy="145" r="143" fill="#ffffff" stroke="var(--rim)" stroke-width="1"/>
    <g clip-path="url(#disc-clip)">
      <rect x="0" y="0" width="290" height="190" fill="url(#disc-ink)" role="img" aria-label="Tintenwolken mit polygonalen Facetten und Profil eines Bandmitglieds"/>
    </g>
    <circle cx="145" cy="145" r="34" fill="var(--canvas)" stroke="var(--rim)" stroke-width="1"/>
    <text class="disc-band" x="148" y="226" text-anchor="middle">LEMURGROOVE</text>
    <text class="disc-release" x="172" y="240" text-anchor="middle">PAPER SAILS</text>
    <text class="disc-tracks">
      <textPath href="#disc-rim" startOffset="4%">1. VELVET STAIR | 2. SHOW US WHY | 3. HARBOR GLOW | 4. CAN WE STAY | 5. QUIET HOURS</textPath>
    </text>
  </svg>

  <section class="panel panel--inside-left" aria-label="Innenseite links">
    <div class="artwork artwork--inside-left" role="img" aria-label="Tintenwolken in Magenta, Rosa, Pfirsich und Indigo mit polygonalen Facetten"></div>
    <p class="lyrics">Skin burned red<br>and scarfes and hats<br>paper sails like ads on TV<br>like leaves in the wind</p>
  </section>

  <section class="panel panel--inside-right" aria-label="Innenseite rechts">
    <div class="artwork artwork--inside-right" role="img" aria-label="Tintenwolken in Pfirsich, Violett und Magenta mit polygonalen Facetten, Hintergrund der CD-Halterung"></div>
  </section>

</main>
</body>
</html>
```